Solar Company Website
The Larkfield Solar Company
• 8 octobre 2010 21:00 quimbrella
what is the meaning of minimalistaic design according to you ??
Please forward all rip off claims to report@quellnary.com
• 7 octobre 2010 08:40 Talvek
I submit my fresh design in a few hours.
• 5 octobre 2010 23:51 Pl4nkWorks
Hi DV,
I have done few changes please have a look give your Feedback.
Many Thanks.
• 5 octobre 2010 20:35 dremlo
I will submit soon my new entry!
• 4 octobre 2010 13:47 Pl4nkWorks
I have design another option please give me feedback.
• 3 octobre 2010 16:39 VelvetTurnip
Hey there, I submitted something a little different for you. I just wanted to say I'm also from Massachusetts and I'm a big fan of new technology that helps the environment. I'd really like to get behind this project. Even if you don't pick my draft, if you need someone who can manage your website, make changes, uploads and that sort of thing I can do that.
• 3 octobre 2010 14:52 dovantrel
Hi, I like most of the designs. But they are all very similar. Nothing yet is 5 stars. Could you try radically new design ideas?
• 2 octobre 2010 13:50 Pl4nkWorks
Please Give Feedback.
Many Thanks
• 2 octobre 2010 11:22 dovantrel
Dear All,
Please submit completely different design ideas. Do not use my stars on my preferred designs as a starting point.
Try to be innovative.
• 2 octobre 2010 05:42 dovantrel
Here are some photos that you can use for design submissions
http://photoshelf.example.net/dovantrel/VerlingSunfair2010?authkey=Kx7tPmQwZa4bN9r12hY5e&feat=directlink
• 1 octobre 2010 01:13 Kobu43
Hi DV, I am waiting for your valuable comments
• 30 septembre 2010 21:40 HollowMarigold
goos. Sheesh. I mean I'm good. Except when I type too fast and didn't proof read! Ack!
• 30 septembre 2010 21:39 HollowMarigold
DV: That link you posted for the logo, brings me back to this page. ?? Hmmmm... Do you have the actual URL or try another link insert? I want to give this a shot. I'm goos with web page design.
• 30 septembre 2010 00:29 Pl4nkWorks
I'm in soon you will my design.
• 29 septembre 2010 14:03 dovantrel
About Us, Residential, Commercial, Solar Basics, Contact Us, Blog
You can use the following URL as an information model:
http://brevanpower.com/home/massachusetts-rhode-island/?state=ma-ri
• 28 septembre 2010 21:51 trasvik
What links would you like in your navigation? About Us, Services, etc...
• 28 septembre 2010 13:20 dovantrel
Hi,
Here is the company logo to be fitted onto website page.
http://photoshelf.example.net/dovantrel/LarkfieldSolar?feat=directlink

```html
<!DOCTYPE html>
<html lang="en">
<head>
<meta charset="utf-8">
<title>Larkfield Solar – Home</title>
<link rel="stylesheet" href="https://fonts.googleapis.com/css2?family=Arimo:wght@400;700&display=swap">
<style>
:root{
  --orange:#e8760c;
  --orange-dark:#c85f05;
  --ink:#333;
  --muted:#666;
  --nav:#3b3b3b;
  --nav-top:#4a4a4a;
  --band:#eeeeee;
  --yellow:#f7b20a;
  --yellow-light:#fbd04a;
  --panel:#4a4a4a;
  --panel-dark:#3a3a3a;
  --field:#f4f4f4;
  --line:#cfcfcf;
}
*{box-sizing:border-box;margin:0;padding:0}
html,body{width:1200px;height:963px;overflow:hidden}
body{background:#fff;font-family:"Arimo",Arial,sans-serif;color:var(--ink);position:relative}
.abs{position:absolute}
a{color:inherit;text-decoration:none}

/* header */
.brand-name{left:135px;top:82px;font-size:22px;font-weight:700;color:#3b3b3b;letter-spacing:.5px}
.account{left:762px;top:24px;font-size:13px;color:#444}
.search{left:898px;top:20px;width:172px;height:26px;border:1px solid #ccc;border-radius:13px;background:#f7f7f7}
.search svg{position:absolute;right:9px;top:6px}
.phone{left:885px;top:56px;font-size:27px;color:#555;display:flex;align-items:center;gap:10px}
.mail{left:918px;top:88px;font-size:13px;color:#555;display:flex;align-items:center;gap:8px}

/* nav */
.nav{left:0;top:130px;width:1200px;height:44px;background:linear-gradient(var(--nav-top),var(--nav))}
.nav ul{list-style:none;position:absolute;left:338px;top:0;display:flex;height:44px;align-items:center;gap:16px}
.nav li{font-size:13px;font-weight:700;color:#fff;padding:4px 8px}
.nav li.current{background:var(--orange);border-radius:3px}

/* hero */
.hero-band{left:0;top:174px;width:1200px;height:277px;background:var(--band)}
.hero-photo{left:135px;top:187px;width:463px;height:260px;background:linear-gradient(#b9d4ec,#7e8f9f 55%,#9a9a94)}
.welcome{left:617px;top:218px;font-size:30px;font-weight:400;color:#444}
.welcome b{color:var(--orange);font-weight:400}
.intro{left:617px;top:270px;width:510px;font-size:12.5px;line-height:16px;color:#555}
.intro p+p{margin-top:14px}
.btn{display:inline-block;background:var(--orange);color:#fff;font-size:12px;font-weight:700;padding:4px 10px;border-radius:10px}
.hero-more{left:617px;top:408px}

/* sidebar */
.newsletter{left:130px;top:468px;width:210px;height:80px;border:1px solid var(--line);background:#fafafa;padding:12px}
.newsletter h3{font-size:13px;color:#333}
.newsletter .field{margin-top:10px;display:flex}
.newsletter .field span{flex:1;height:24px;background:#fff;border:1px solid #ccc}
.newsletter .field i{width:32px;height:24px;background:var(--orange);display:flex;align-items:center;justify-content:center}
.contact{left:130px;top:556px;width:210px}
.contact h2{font-size:27px;color:#333}
.contact .sub{font-size:13px;color:#555;margin:2px 0 10px}
.contact .input{height:21px;border:1px solid #ccc;background:var(--field);font-size:11px;color:#888;padding:3px 6px;margin-bottom:7px}
.contact .area{height:42px}
.contact .submit{margin:8px 0 0 76px;display:inline-block;border:1px solid var(--orange);color:var(--orange);font-size:12px;font-weight:700;padding:3px 8px;border-radius:3px}
.social{left:168px;top:795px;display:flex;gap:14px}
.social span{width:22px;height:22px;background:#7a8fa8;border-radius:3px}

/* why choose */
.why{left:351px;top:450px;width:789px;height:175px;background:radial-gradient(circle at 20% 40%,var(--yellow-light),var(--yellow) 70%)}
.why h2{position:absolute;left:16px;top:12px;font-size:24px;font-weight:400;color:#fff}
.why ul{list-style:none;position:absolute;left:18px;top:58px;width:340px}
.why li{font-size:12px;line-height:15px;color:#4a3500;padding-left:16px;position:relative;margin-bottom:7px}
.why li svg{position:absolute;left:0;top:1px}
.why .more{position:absolute;left:18px;top:150px;font-size:12px;font-weight:700;color:#333}
.why-photo{position:absolute;right:0;top:20px;width:370px;height:155px;background:linear-gradient(135deg,#fbd04a,#6d8fbf 45%,#2f4a78)}

/* services */
.services{left:351px;top:625px;width:789px;height:221px;background:linear-gradient(var(--panel),var(--panel-dark))}
.service{position:absolute;top:0;width:355px}
.service h3{font-size:24px;font-weight:400;color:#fff;padding:12px 8px 0}
.service .thumb{position:absolute;left:12px;top:50px;width:112px;height:150px;border:3px solid #fff}
.service .text{position:absolute;left:135px;top:50px;width:205px;font-size:11.5px;line-height:14px;color:#eee}
.service .text p+p{margin-top:10px}
.service .more{display:inline-block;margin-top:10px;font-weight:700;color:#fff}
.residential{left:0}
.commercial{left:380px}
.divider{position:absolute;left:358px;top:0;width:14px;height:221px;background:#2e2e2e}

/* footer */
.foot-rule{left:0;top:886px;width:1200px;height:1px;background:#ddd}
.footer-links{left:130px;top:898px;font-size:12px;color:#444}
.copyright{left:130px;top:917px;font-size:12px;color:#444}
.footer-brand{left:960px;top:908px;font-size:20px;font-weight:700;color:#d8d8d8}
</style>
</head>
<body>

<header>
  <div class="abs brand-name">LARKFIELD SOLAR</div>
  <div class="abs account"><a href="#">Login</a> &nbsp;|&nbsp; <a href="#">Register</a></div>
  <div class="abs search">
    <svg width="13" height="13" viewBox="0 0 13 13"><circle cx="5.5" cy="5.5" r="4" fill="none" stroke="#777" stroke-width="1.6"/><line x1="8.5" y1="8.5" x2="12" y2="12" stroke="#777" stroke-width="1.8"/></svg>
  </div>
  <div class="abs phone">
    <svg width="22" height="24" viewBox="0 0 22 24"><path d="M5 2 L9 2 L10 8 L7 10 Q9 15 13 18 L15 15 L21 17 L20 22 Q10 23 4 12 Q1 6 5 2Z" fill="#666"/></svg>
    000 0000 0000
  </div>
  <div class="abs mail">
    <svg width="16" height="12" viewBox="0 0 16 12"><rect x=".5" y=".5" width="15" height="11" fill="none" stroke="#666"/><path d="M.5 .5 L8 7 L15.5 .5" fill="none" stroke="#666"/></svg>
    info@larkfieldsolar.com
  </div>
</header>

<nav class="abs nav">
  <ul>
    <li class="current">Home</li>
    <li>About Larkfield Solar</li>
    <li>Residential</li>
    <li>Commercial</li>
    <li>Solar Basics</li>
    <li>Our Blog</li>
    <li>Contact Us</li>
  </ul>
</nav>

<section>
  <div class="abs hero-band"></div>
  <div class="abs hero-photo" role="img" aria-label="Visitors standing under a large solar panel canopy at a trade fair"></div>
  <h1 class="abs welcome">Welcome to <b>LARKFIELD SOLAR</b></h1>
  <div class="abs intro">
    <p>Lorem ipsum dolor sit amet, consectetur adipiscing elit. Sed lobortis ligula ut nibh adipiscing congue. Pellentesque habitant morbi tristique senectus et netus et malesuada fames ac turpis egestas. Suspendisse lacinia pretium metus sed tincidunt.</p>
    <p>Cras odio nibh, malesuada vitae feugiat quis, adipiscing quis enim. Vestibulum ante ipsum primis in faucibus orci luctus et ultrices posuere cubilia Curae; In tincidunt, dui ut ultricies iaculis, nisl felis pulvinar lectus, viverra ornare nunc.</p>
  </div>
  <a class="abs btn hero-more" href="#">Read More</a>
</section>

<aside>
  <div class="abs newsletter">
    <h3>Subscribe to our Newsletter</h3>
    <div class="field"><span></span><i><svg width="10" height="10" viewBox="0 0 10 10"><path d="M2 1 L8 5 L2 9Z" fill="#fff"/></svg></i></div>
  </div>
  <div class="abs contact">
    <h2>CONTACT US</h2>
    <p class="sub">Get in Touch with Larkfield Solar</p>
    <div class="input">Name</div>
    <div class="input">Phone</div>
    <div class="input">Email Address</div>
    <div class="input area">Comments</div>
    <span class="submit">SUBMIT</span>
  </div>
  <div class="abs social"><span></span><span></span><span></span><span></span></div>
</aside>

<section class="abs why">
  <h2>Why Choose Larkfield Solar</h2>
  <ul>
    <li><svg width="10" height="12" viewBox="0 0 10 12"><path d="M6 0 L1 7 L5 7 L3 12 L9 4 L5 4Z" fill="#c85f05"/></svg>Sed facilisis ligula at nibh dapibus lacinia elementum arcu vehicula.</li>
    <li><svg width="10" height="12" viewBox="0 0 10 12"><path d="M6 0 L1 7 L5 7 L3 12 L9 4 L5 4Z" fill="#c85f05"/></svg>Duis sit amet nunc sed magna condimentum malesuada non eget felis.</li>
    <li><svg width="10" height="12" viewBox="0 0 10 12"><path d="M6 0 L1 7 L5 7 L3 12 L9 4 L5 4Z" fill="#c85f05"/></svg>Nullam bibendum sapien id velit lobortis gravida.</li>
  </ul>
  <a class="more" href="#">Read More</a>
  <div class="why-photo" role="img" aria-label="Rows of solar panels against a blue sky"></div>
</section>

<section class="abs services">
  <article class="service residential">
    <h3>Larkfield Solar Residential</h3>
    <div class="thumb" role="img" aria-label="Solar panels mounted on a house roof" style="background:linear-gradient(#6d9bd6,#b8533a)"></div>
    <div class="text">
      <p>Lorem ipsum dolor sit amet consectetur adipiscing elit. Sed lobortis ligula ut nibh adipiscing congue.</p>
      <p>Pellentesque habitant morbi tristique senectus et netus et malesuada.</p>
      <a class="more" href="#">Read More</a>
    </div>
  </article>
  <div class="divider"></div>
  <article class="service commercial">
    <h3>Larkfield Solar Commercial</h3>
    <div class="thumb" role="img" aria-label="Solar array on a commercial building" style="background:linear-gradient(#3f6fb8,#9bb4cf)"></div>
    <div class="text">
      <p>Lorem ipsum dolor sit amet consectetur adipiscing elit. Sed lobortis ligula ut nibh adipiscing congue.</p>
      <p>Pellentesque habitant morbi tristique senectus et netus et malesuada.</p>
      <a class="more" href="#">Read More</a>
    </div>
  </article>
</section>

<footer>
  <div class="abs foot-rule"></div>
  <p class="abs footer-links">Home &nbsp;|&nbsp; About Larkfield Solar &nbsp;|&nbsp; Residential &nbsp;|&nbsp; Commercial &nbsp;|&nbsp; Solar Basics &nbsp;|&nbsp; Our Blog &nbsp;|&nbsp; Contact Us</p>
  <p class="abs copyright">Copyright © 2009, Larkfield Solar Company. All rights Reserved</p>
  <p class="abs footer-brand">LARKFIELD SOLAR</p>
</footer>

</body>
</html>
```